I need new business cards for my webb agency.

We need front AND backside.

Front:
Name, Title, company name, www, email, adress, phone 1, skype,

Back:
Logo + We will use promo text about what we do i.e. Web design, Search engine marketing, Advertisements & Web analytics

We want to look like a young and creative web agency. Business card should match our logo and colors. Please new this is a new logo enclosed which we are not using anywhere yet.

We will print on solid quality paper.

www.plumvantix.com

Marrowfield Suites 10 th fl.
42/16 Tarnawell Soi 8
Bangkok 10110
Thailand
+66 (0) 2-487-6031

```html
<!DOCTYPE html>
<html lang="en">
<head>
<meta charset="utf-8">
<title>Plumvantix business cards</title>
<link rel="stylesheet" href="https://fonts.googleapis.com/css2?family=Arimo:wght@400;700&display=swap">
<style>
  :root {
    --stage: #e9e9e9;
    --paper: #ffffff;
    --ink: #222222;
    --brand-dark: #3b2a20;
    --brand-orange: #f08a1c;
  }
  html, body { margin: 0; padding: 0; overflow: hidden; }
  body {
    width: 1200px; height: 900px;
    background: var(--stage);
    font-family: "Arimo", Arial, sans-serif;
    color: var(--ink);
    position: relative;
  }
  .card {
    position: absolute;
    left: 280px;
    width: 640px; height: 366px;
    background: var(--paper);
    box-shadow: 0 4px 14px rgba(0,0,0,0.18);
  }
  .card--back { top: 60px; }
  .card--front { top: 474px; }

  .brand {
    position: absolute; left: 40px; top: 218px;
    display: flex; align-items: center; gap: 12px;
  }
  .brand__name {
    font-weight: 700; font-size: 50px; letter-spacing: 1px;
    color: var(--brand-dark); line-height: 1;
  }
  .brand__dot {
    width: 40px; height: 40px; border-radius: 50%;
    background: var(--brand-orange);
  }
  .tagline {
    position: absolute; left: 42px; top: 286px;
    font-size: 14px; font-weight: 700; color: var(--ink);
  }

  .person {
    position: absolute; left: 300px; top: 150px; text-align: center;
  }
  .person__name { font-size: 21px; font-weight: 700; margin: 0; }
  .person__title { font-size: 12px; font-weight: 700; margin: 4px 0 0 60px; }

  .contacts {
    position: absolute; left: 40px; top: 244px;
    list-style: none; margin: 0; padding: 0;
    font-size: 14px; line-height: 20px;
  }
  .contacts li { display: flex; align-items: flex-start; gap: 10px; }
  .contacts svg { width: 12px; height: 12px; margin-top: 4px; flex: none; fill: var(--brand-orange); }
</style>
</head>
<body>
  <section class="card card--back" aria-label="Card back">
    <div class="brand">
      <span class="brand__name">PLUMVANTIX</span>
      <span class="brand__dot"></span>
    </div>
    <p class="tagline">Web design, Search engine marketing, Advertisements, Web analytics</p>
  </section>

  <section class="card card--front" aria-label="Card front">
    <div class="person">
      <p class="person__name">Tomasz Wrelnik</p>
      <p class="person__title">Founder</p>
    </div>
    <ul class="contacts">
      <li>
        <svg viewBox="0 0 12 12"><path d="M2.5 0.5 L4.5 0.5 L5.2 3.2 L3.8 4.2 Q5 7 7.8 8.2 L8.8 6.8 L11.5 7.5 L11.5 9.5 Q11 11.5 9 11.5 Q1 10.5 0.5 3 Q0.5 1 2.5 0.5Z"/></svg>
        <span>+66 (0) 2-487-6031</span>
      </li>
      <li>
        <svg viewBox="0 0 12 12"><path d="M0 2 H12 V10 H0Z M0.8 2.6 L6 6.6 L11.2 2.6" stroke="#fff" stroke-width="0.9"/></svg>
        <span>hello@plumvantix.com</span>
      </li>
      <li>
        <svg viewBox="0 0 12 12"><circle cx="6" cy="6" r="6"/></svg>
        <span>plumvantix 001</span>
      </li>
      <li>
        <svg viewBox="0 0 12 12"><circle cx="6" cy="6" r="6"/><path d="M0 6 H12 M6 0 V12 M6 0 Q2 6 6 12 M6 0 Q10 6 6 12" stroke="#fff" stroke-width="0.8" fill="none"/></svg>
        <span>www.plumvantix.com</span>
      </li>
      <li>
        <svg viewBox="0 0 12 12"><path d="M6 0.5 L12 6 H10.2 V11.5 H7.3 V8 H4.7 V11.5 H1.8 V6 H0Z"/></svg>
        <span>Marrowfield Suites 10 th fl.<br>42/16 Tarnawell Soi 8, Bangkok 10110, Thailand</span>
      </li>
    </ul>
  </section>
</body>
</html>
```